Corwin Ashby Foundation Flyer

Design a two sided flyer that will be used to solicit charitable donations from local residents and businesses for a new school gymnasium. The fundraising project is being done by the Corwin Ashby Foundation. I have attached two files for: 1. "Original" Flyer 2. "Revised" Copy. Please use "revised" for the copy. You can refer to "original" for illustrations and pictures. The Corwin Ashby Foundation does not have a logo, so you can create one. It should be simple and understated.

```html
<!DOCTYPE html>
<html lang="en">
<head>
<meta charset="utf-8">
<title>Corwin Ashby Foundation Flyer</title>
<link href="https://fonts.googleapis.com/css2?family=Oswald:wght@400;500;600&family=Poppins:wght@400;500;600;700&family=Montserrat:wght@400;500;700&family=Allura&display=swap" rel="stylesheet">
<style>
:root{
  --ink:#121212;
  --gold:#d8c797;
  --gold-deep:#9a8657;
  --cream:#eee2c1;
  --paper:#ffffff;
  --stage:#c9c9c9;
  --muted:#2a2a2a;
}
*{margin:0;padding:0;box-sizing:border-box}
html,body{width:1200px;height:803px;overflow:hidden;background:var(--stage)}
body{position:relative;font-family:"Poppins",sans-serif;color:var(--ink)}
.page{position:absolute;top:72px;width:488px;height:631px;background:var(--paper);overflow:hidden}
.page--front{left:73px}
.page--back{left:616px}
.abs{position:absolute}
.body-copy{font-size:7px;line-height:8.6px;color:var(--muted)}
.photo{position:absolute}

/* front */
.brand-mark{left:97px;top:27px;width:58px;height:57px;background:var(--ink)}
.brand-name{left:30px;top:90px;width:192px;text-align:center;font-family:"Oswald",sans-serif;font-weight:500;font-size:26px;line-height:30px;letter-spacing:.5px}
.brand-sub{left:30px;top:121px;width:192px;text-align:center;font-family:"Oswald",sans-serif;font-weight:500;font-size:8px;letter-spacing:5px}
.title-box{left:28px;top:145px;width:268px;height:127px;background:var(--ink);color:#fff;padding:15px 0 0 13px;white-space:nowrap}
.title-lift{font-family:"Montserrat",sans-serif;font-weight:500;font-size:19px;letter-spacing:4.5px;line-height:21px}
.title-main{font-family:"Oswald",sans-serif;font-weight:500;color:var(--gold);font-size:24px;line-height:31px;letter-spacing:-.4px}
.title-legacy{font-family:"Montserrat",sans-serif;font-size:12.5px;letter-spacing:3.6px;line-height:16px}
.title-name{font-family:"Poppins",sans-serif;font-weight:600;font-size:18px;line-height:22px;margin-top:9px;letter-spacing:.3px}
.section-head{font-weight:600;font-size:14.5px}
.lead-head{font-weight:600;font-size:9.5px}
.why-band{left:28px;top:360px;width:433px;height:129px}
.why-tab{left:12px;top:4px;color:#fff;font-weight:600;font-size:9px}
.why-col{top:29px;width:198px}
.why-col b{font-weight:600;color:var(--ink)}
.pay-head{left:27px;top:506px;font-family:"Oswald",sans-serif;font-weight:500;font-size:21px;line-height:22px;transform:scaleX(.92);transform-origin:left}
.pay-head span{color:var(--gold-deep)}

/* footer */
.footer{left:0;top:565px;width:488px;height:66px;background:var(--ink);color:#fff}
.f-label{left:27px;top:11px;font-family:"Oswald",sans-serif;color:var(--gold);font-size:11px;line-height:13px;letter-spacing:.3px}
.f-label small{display:block;color:#fff;font-family:"Montserrat",sans-serif;font-size:7.8px;letter-spacing:.8px;line-height:11px}
.f-icon{width:9px;height:9px;border-radius:50%;background:var(--gold)}
.f-name{left:176px;top:9px;color:var(--gold);font-weight:600;font-size:9.6px;line-height:13px}
.f-name em{font-style:normal;color:#ddd;font-family:"Montserrat",sans-serif;font-weight:400;font-size:6.6px;letter-spacing:1.4px;margin-left:3px}
.f-org{left:176px;top:22px;font-weight:600;font-size:7px}
.f-contact{left:356px;font-weight:600;font-size:8px}

/* back */
.help-box{left:27px;top:27px;width:433px;height:122px}
.help-head{left:20px;top:13px;color:#fff;font-weight:600;font-size:14px;letter-spacing:.3px}
.help-head span{color:var(--gold)}
.help-copy{left:20px;top:36px;width:205px;color:#fff;font-size:9px;line-height:10.5px}
.donate-item{left:66px;width:178px}
.donate-item b{font-weight:600;font-size:7.6px;display:block;line-height:9px}
.donate-item p{font-size:7.8px;line-height:9.6px}
.divider{left:66px;width:178px;height:1px;background:#cfcfcf}
.d-icon{left:27px;width:24px;height:24px;border-radius:50%}
.events-box{left:27px;top:330px;width:216px;height:216px}
.events-head{left:12px;top:14px;font-weight:700;font-size:10.6px;line-height:13px}
.join-script{left:9px;top:39px;font-family:"Allura",cursive;font-size:18px;line-height:20px}
.join-copy{left:60px;top:41px;font-size:7.6px;line-height:9.6px;width:150px}
.follow-band{left:24px;top:398px;width:200px;height:36px;background:var(--ink);color:#fff;font-weight:600;font-size:10.8px;line-height:13px;padding:5px 0 0 14px}
.stay-head{left:39px;top:444px;font-weight:600;font-size:11.6px}
.stay-copy{left:39px;top:467px;width:175px;font-size:7.8px;line-height:9.6px}
.social-head{left:39px;top:499px;font-weight:600;font-size:10.6px}
.social-name{left:57px;top:517px;font-size:11px}
.spons-head{left:263px;top:265px;font-weight:600;font-size:11.6px}
.spons-copy{left:263px;top:287px;width:194px;font-size:8.2px;line-height:9.6px}
.phone-pill{left:352px;top:347px;width:86px;height:13px;border-radius:3px;background:var(--ink);color:#fff;font-weight:600;font-size:9.2px;line-height:13px;text-align:center}
.quote-box{left:263px;top:390px;width:198px;height:156px;border:1px solid #555;border-radius:0 0 0 6px}
.quote-copy{left:12px;top:12px;width:170px;font-size:8px;line-height:9.6px}
.quote-thanks{left:12px;top:117px;font-weight:600;font-size:7.8px}
.quote-sign{left:12px;top:128px;font-family:"Allura",cursive;font-size:16px;white-space:nowrap}
.qmark{font-family:"Poppins",sans-serif;font-size:26px;font-weight:400;line-height:26px;background:#fff;padding:0 3px}
</style>
</head>
<body>

<section class="page page--front">
  <div class="abs brand-mark"></div>
  <div class="abs brand-name">CORWIN ASHBY</div>
  <div class="abs brand-sub">FOUNDATION</div>

  <div class="photo" role="img" aria-label="Photo of young gymnasts in leotards stretching at a barre" style="left:269px;top:27px;width:191px;height:207px;background:linear-gradient(160deg,#dcd6cf 0%,#b9a58a 45%,#8d7760 100%)"></div>
  <svg class="abs" style="left:269px;top:27px" width="60" height="70" viewBox="0 0 60 70"><polygon points="0,15 60,0 0,70" fill="#121212"/></svg>

  <div class="abs title-box">
    <div class="title-lift">LIFTING OUR</div>
    <div class="title-main">COMMUNITY &amp; HONORING</div>
    <div class="title-legacy">THE LIFE AND LEGACY OF</div>
    <div class="title-name">| CORWIN ASHBY</div>
  </div>

  <h2 class="abs section-head" style="left:310px;top:246px">The Vision</h2>
  <p class="abs body-copy" style="left:310px;top:272px;width:153px">The Corwin Ashby Memorial Gymnasium Concept will be an onsite facility that will be approximately 12,000 square feet and will cost $4.5 million. Attached directly to the school it will include a gymnasium with proper room for spectators, entry lobby, concession area, two team locker rooms and an equipment storage room.</p>

  <h3 class="abs lead-head" style="left:28px;top:282px">Dear Community Members, Friends and Supporters</h3>
  <p class="abs body-copy" style="left:28px;top:300px;width:265px">We invite you to join us in this journey of love and community that celebrates the life and legacy of a beloved local resident, Corwin Ashby. Corwin’s unwavering love for Linden Island and his profound belief in the power of community has inspired us to embark on this heartfelt initiative to build a new school gymnasium in his honor.</p>

  <div class="abs why-band">
    <svg class="abs" style="left:0;top:0" width="433" height="129" viewBox="0 0 433 129">
      <polygon points="0,0 410,0 433,17 433,129 0,129" fill="#eee2c1"/>
      <polygon points="0,0 410,0 412,2 175,2 160,20 0,20" fill="#121212"/>
    </svg>
    <div class="abs why-tab">Why Build a Gymnasium?</div>
    <p class="abs why-col body-copy" style="left:12px"><b>One small community can come together in support of our Island youth.</b><br>In July 2023, our community tragically lost Corwin Ashby in a horrific motorcycle accident. In tribute to Corwin’s remarkable spirit and love for the Linden Island school, the Corwin Ashby Foundation (a 501(c)(3) foundation) is seeking to lift our community and provide a much-needed facility for our community and students by building a much needed school gymnasium in Corwin’s honor.</p>
    <p class="abs why-col body-copy" style="left:220px;width:195px">Currently, the school district doesn’t have an onsite gym. Students hold gym classes, practices, and scrimmages at a rented community gym which is a short walk from the school. The new gymnasium would benefit the students and community as well as serve as a living memorial to Corwin and other students who left us far too soon. The new gym will be a place for our Island youth to have physical education classes as well as a place for our student-athletes to compete and host visiting teams.</p>
  </div>

  <h2 class="abs pay-head">WHY CAN’T THE<br><span>SCHOOL PAY?</span></h2>
  <p class="abs body-copy" style="left:150px;top:506px;width:312px">The combination of revenue limits and sparse state aid has left many Northland schools unable to meet their operational needs. Linden Island is one of the state’s most severely underfunded school districts! This is NOT because they overspend but because they are severely underfunded. The school has no choice but to run on a bare-bones budget.</p>

  <footer class="abs footer">
    <div class="abs f-label">FOR MORE INFORMATION<small>PLEASE REACH OUT TO:</small></div>
    <div class="abs f-icon" style="left:161px;top:11px"></div>
    <div class="abs f-name">DANA ASHBY<em>PRESIDENT</em></div>
    <div class="abs f-org">Corwin Ashby Memorial Foundation</div>
    <div class="abs f-icon" style="left:345px;top:10px"></div>
    <div class="abs f-contact" style="top:8px">555-014-2290</div>
    <div class="abs f-icon" style="left:345px;top:22px"></div>
    <div class="abs f-contact" style="top:20px">info@corwinashby.org</div>
  </footer>
</section>

<section class="page page--back">
  <div class="abs help-box">
    <svg class="abs" style="left:0;top:0" width="433" height="122" viewBox="0 0 433 122"><polygon points="0,0 409,0 433,27 433,122 0,122" fill="#121212"/></svg>
    <h2 class="abs help-head">HOW YOU <span>CAN HELP</span></h2>
    <p class="abs help-copy">To bring this vision to life, we need your help! We’re reaching out to ask for your generous donations to help fund the gym’s construction. Your contribution will not only honor Corwin’s memory but will also create a lasting legacy that benefits our Island, our Students and our community.</p>
  </div>

  <svg class="abs" style="left:284px;top:39px" width="164" height="213" viewBox="0 0 164 213"><polygon points="0,0 150,0 164,14 164,213 0,213" fill="#fff" stroke="#333" stroke-width="1"/></svg>
  <div class="photo" role="img" aria-label="Photo of young girls in ballet clothes practising at a dance barre" style="left:289px;top:44px;width:154px;height:203px;background:linear-gradient(170deg,#e9eaec 0%,#c9c9cc 50%,#8f8f96 100%);clip-path:polygon(0 0,91% 0,100% 7%,100% 100%,0 100%)"></div>

  <h2 class="abs" style="left:27px;top:161px;font-weight:600;font-size:13px">Ways to Donate</h2>

  <div class="abs d-icon" style="left:27px;top:181px;background:var(--cream);border:2px solid #fff;box-shadow:0 0 0 1px var(--gold)"></div>
  <div class="abs donate-item" style="top:184px"><b>Online</b><p>Mobile pay (address to come)</p></div>
  <div class="abs divider" style="top:207px"></div>

  <div class="abs d-icon" style="left:27px;top:217px;background:#fff;border:3px solid var(--ink)"></div>
  <div class="abs donate-item" style="top:213px"><b>In-Person</b><p>Donations can be made at the front office of the Linden Island School, located at 412 Harbor Road.</p></div>
  <div class="abs divider" style="top:256px"></div>

  <div class="abs d-icon" style="left:27px;top:262px;background:var(--cream);border:2px solid #fff;box-shadow:0 0 0 1px var(--gold)"></div>
  <div class="abs donate-item" style="top:261px"><b>Mail</b><p>Send checks payable to<br><b style="display:inline;font-size:7.8px">"Corwin Ashby Foundation"</b> to</p>
    <p style="padding-left:11px;position:relative"><svg style="position:absolute;left:0;top:1px" width="6" height="8" viewBox="0 0 6 8"><path d="M3 0a3 3 0 0 1 3 3c0 2-3 5-3 5S0 5 0 3a3 3 0 0 1 3-3z" fill="#d62828"/><circle cx="3" cy="3" r="1" fill="#fff"/></svg>P.O. Box 318, Linden Island,<br>NL 50417</p>
  </div>

  <div class="abs events-box">
    <svg class="abs" style="left:0;top:0" width="216" height="216" viewBox="0 0 216 216"><polygon points="0,0 195,0 216,21 216,216 0,216" fill="#eee2c1"/></svg>
    <h3 class="abs events-head">UPCOMING FUNDRAISING<br>EVENTS</h3>
    <div class="abs join-script">Join us</div>
    <p class="abs join-copy">For a series of events to raise funds and celebrate Corwin’s life</p>
  </div>
  <div class="abs follow-band">Follow our Community Page for<br>updates and events</div>
  <h3 class="abs stay-head">Stay Connected</h3>
  <p class="abs stay-copy">Follow our progress and stay updated on upcoming events by visiting our website and following us on social media.</p>
  <h3 class="abs social-head">Community Page</h3>
  <div class="abs social-name">Corwin Ashby Foundation</div>

  <h2 class="abs spons-head">Sponsorship Opportunities</h2>
  <p class="abs spons-copy">We also offer sponsorship opportunities for individuals and businesses looking to make a significant impact. Sponsorships for various areas within the gymnasium and special recognition in our community events are available. For more information on sponsorships,</p>
  <p class="abs" style="left:263px;top:350px;font-size:7.8px">please contact us at</p>
  <div class="abs phone-pill">(555) 208-7731</div>
  <p class="abs" style="left:263px;top:365px;font-size:7.8px;font-weight:500">or email info@corwinashbyfoundation.org.</p>

  <div class="abs quote-box">
    <p class="abs quote-copy">Corwin Ashby’s legacy is one of vitality, inspiration, and Island Community Spirit. Let’s honor him by creating a place where his values continue to thrive and where everyone can feel good about our Island Community and meet the needs of our children and students. Your support is crucial to making this dream a reality. Thank you for your generosity &amp; commitment to our community.</p>
    <p class="abs quote-thanks">With heartfelt gratitude,</p>
    <p class="abs quote-sign">The Corwin Ashby Foundation</p>
  </div>
  <div class="abs qmark" style="left:259px;top:378px">“</div>
  <div class="abs qmark" style="left:446px;top:529px">”</div>

  <footer class="abs footer">
    <div class="abs f-label">FOR MORE INFORMATION<small>PLEASE REACH OUT TO:</small></div>
    <div class="abs f-icon" style="left:161px;top:11px"></div>
    <div class="abs f-name">DANA ASHBY<em>PRESIDENT</em></div>
    <div class="abs f-org">Corwin Ashby Memorial Foundation</div>
    <div class="abs f-icon" style="left:345px;top:10px"></div>
    <div class="abs f-contact" style="top:8px">555-014-2290</div>
    <div class="abs f-icon" style="left:345px;top:22px"></div>
    <div class="abs f-contact" style="top:20px">info@corwinashby.org</div>
  </footer>
</section>

</body>
</html>
```